Brightmoor Dental Care Stationery

create stationery, business cards and envelops for business. Use current logo on website but open to new fonts for the business name. Business name is Brightmoor Dental Care, would like below the name added "Cosmetic - Family - Implants" Website is www.brightmoordentalcareXQ.example. I would like to have modern look, clean, and professional. The water mark of the logo is a great thing to ad as well.

Target Market(s)

General public, Families, Cosmetic, Implant

Industry/Entity Type

Dental

Font styles to use
Sans Serif

Colors
9bcb3c
000000
757575
c9c9c9

Requirements
Must have
• Would like to see different versions of the current logo. Improvements, color, sytle, and class.
Nice to have
• current font has double "oo" in the Brightmoor logo, does not need to have with new logo.

```html
<!DOCTYPE html>
<html lang="en">
<head>
<meta charset="utf-8">
<title>Brightmoor Dental Care – Business Card</title>
<link rel="stylesheet" href="https://fonts.googleapis.com/css2?family=PT+Sans:wght@400;700&display=swap">
<style>
  :root {
    --backdrop: #e4e4e4;
    --card-white: #ffffff;
    --card-slate: #323a45;
    --brand-green: #8cc43f;
    --ink: #2b2f36;
    --ink-soft: #3d4148;
    --grey: #757575;
    --rule: #8a8a8a;
    --watermark: #46505c;
  }
  * { margin: 0; padding: 0; box-sizing: border-box; }
  html, body { width: 1200px; height: 987px; overflow: hidden; }
  body {
    background: var(--backdrop);
    font-family: "PT Sans", "Helvetica Neue", Arial, sans-serif;
    position: relative;
  }
  .card {
    position: absolute;
    left: 293px;
    width: 615px;
    height: 349px;
    box-shadow: 0 2px 5px rgba(0,0,0,0.18);
    overflow: hidden;
  }
  .card--front { top: 131px; background: var(--card-white); }
  .card--back  { top: 506px; background: var(--card-slate); }

  /* Front: brand block */
  .brand {
    position: absolute;
    right: 36px;
    top: 40px;
    display: flex;
    align-items: center;
    gap: 14px;
  }
  .brand__dot {
    width: 46px; height: 46px;
    border-radius: 50%;
    border: 3px solid var(--brand-green);
  }
  .brand__text { text-align: left; }
  .brand__name {
    font-weight: 700;
    font-size: 27px;
    line-height: 28px;
    color: var(--ink);
    letter-spacing: 0.5px;
  }
  .brand__tagline {
    font-weight: 700;
    font-size: 11.5px;
    color: var(--grey);
    letter-spacing: 1.2px;
    margin-top: 4px;
  }

  /* Front: person */
  .person { position: absolute; left: 35px; top: 186px; }
  .person__name { color: var(--brand-green); font-size: 21px; font-weight: 700; line-height: 24px; }
  .person__role { color: var(--ink-soft); font-size: 16px; margin-top: 6px; }
  .divider {
    position: absolute;
    left: 35px; right: 40px;
    top: 246px;
    height: 1px;
    background: var(--rule);
  }
  .contacts {
    position: absolute;
    left: 35px; top: 256px;
    list-style: none;
    font-size: 15px;
    color: var(--ink-soft);
  }
  .contacts li { display: flex; align-items: center; gap: 8px; height: 23.5px; }
  .contacts svg { width: 14px; height: 14px; fill: var(--brand-green); flex: none; }
  .address {
    position: absolute;
    right: 35px; top: 278px;
    text-align: right;
    font-size: 15px;
    line-height: 23.5px;
    color: var(--ink-soft);
    font-style: normal;
  }

  /* Back */
  .watermark {
    position: absolute;
    left: 16px; top: 16px;
    width: 300px; height: 300px;
    border-radius: 50%;
    background: var(--watermark);
    opacity: 0.55;
  }
  .back-brand {
    position: absolute;
    right: 44px;
    top: 210px;
    text-align: right;
  }
  .back-brand__name {
    color: #ffffff;
    font-weight: 700;
    font-size: 34px;
    line-height: 36px;
    letter-spacing: 0.5px;
  }
  .back-brand__tagline {
    color: #ffffff;
    font-weight: 700;
    font-size: 12.5px;
    letter-spacing: 1.6px;
    margin-top: 4px;
  }
  .back-brand__web { color: #ffffff; font-size: 15px; margin-top: 2px; }
</style>
</head>
<body>

<section class="card card--front" aria-label="Business card front">
  <div class="brand">
    <span class="brand__dot"></span>
    <div class="brand__text">
      <div class="brand__name">BRIGHTMOOR<br>DENTAL CARE</div>
      <div class="brand__tagline">COSMETIC - FAMILY - IMPLANTS</div>
    </div>
  </div>

  <div class="person">
    <div class="person__name">Dr. Martin Calloway D.D.S.</div>
    <div class="person__role">Fairhaven Cosmetic, Family, &amp; Sedation Dentist</div>
  </div>

  <div class="divider"></div>

  <ul class="contacts">
    <li>
      <svg viewBox="0 0 24 24" aria-hidden="true"><path d="M6.6 10.8c1.4 2.8 3.8 5.1 6.6 6.6l2.2-2.2c.3-.3.7-.4 1-.2 1.1.4 2.3.6 3.6.6.6 0 1 .4 1 1V20c0 .6-.4 1-1 1C10.6 21 3 13.4 3 4c0-.6.4-1 1-1h3.5c.6 0 1 .4 1 1 0 1.3.2 2.5.6 3.6.1.3 0 .7-.2 1L6.6 10.8z"/></svg>
      555-014-2260
    </li>
    <li>
      <svg viewBox="0 0 24 24" aria-hidden="true"><path d="M2 5h20v14H2z M2 5l10 8 10-8" /></svg>
      martin@brightmoordentalcareXQ.example
    </li>
    <li>
      <svg viewBox="0 0 24 24" aria-hidden="true"><circle cx="12" cy="12" r="10"/></svg>
      www.brightmoordentalcareXQ.example
    </li>
  </ul>

  <address class="address">418 S Alder Ln<br>Fairhaven, XQ 00000-1234</address>
</section>

<section class="card card--back" aria-label="Business card back">
  <div class="watermark"></div>
  <div class="back-brand">
    <div class="back-brand__name">BRIGHTMOOR<br>DENTAL CARE</div>
    <div class="back-brand__tagline">COSMETIC - FAMILY - IMPLANTS</div>
    <div class="back-brand__web">www.brightmoordentalcareXQ.example</div>
  </div>
</section>

</body>
</html>
```